Door Hanger Design for Electricians Serving Homes

I would like our logo incorporated into the door hanger. We would like a place for a tear off section on the bottom of the hanger with our contact information: K&T Electric - (555) 318-4702 - www.kandtelectric.example - info@kandtelectric.example.
Door Hanger Script
Front Side of the Door Hanger:
[Company Logo]
Need a Reliable Electrician?
Your Local Electrical Expert is Just Around the Corner!
• Quick Response Times
• Affordable Rates
• Quality Workmanship
• Fully Licensed & Insured
• Special Offer:
• 10% OFF Your First Service Call!
Back Side of the Door Hanger:
Don't Let Electrical Issues Keep You in the Dark!
From flickering lights to complete system upgrades, we've got all your
residential electrical needs covered. Our services include:
• Electrical Repairs & Troubleshooting
• Lighting Installation & Upgrades
• Safety Inspections & Code Compliance
• Energy-Efficient Solutions
• 24/7 Emergency Services
• Why Choose Us?
• Friendly, Local Service
• Over 30 Years of Experience
• Satisfaction Guaranteed
• Upfront Pricing
Call Us Today: [Your Phone Number]
Visit Our Website: [Your Website]
Book Your Appointment Now and Claim Your 10% Discount!
Offer valid for new customers on the first visit only. Mention this door hanger when
booking.
[Your Company Name and Contact Information]
Follow Us on Social Media for More Tips and Special Offers!
[Icons for social media platforms: Chatterpage, Pixmosaic, Quibbler, etc.]
Design Tips:
Use bold, clear fonts for easy reading.
Incorporate your brand colors and logo for instant recognition.
Include a clear call to action (CTA) on both sides.
Add a tear-off section at the bottom with your contact information for
convenience.
Use high-quality images or graphics related to electrical work to catch
the eye.
This door hanger design and copy aim to attract residential clients by
highlighting the benefits of your electrical services, special offers, and
how they can easily get in touch with you for their electrical needs.
The door knocker template will have three of the same design on front and three of the same design on the back. This template is from the print shop.

```html
<!DOCTYPE html>
<html lang="en">
<head>
<meta charset="utf-8">
<title>K&amp;T Electric Door Hanger</title>
<link rel="stylesheet" href="https://fonts.googleapis.com/css2?family=DM+Serif+Display&family=Righteous&family=Montserrat:wght@600;700;800&family=Arimo:wght@400;600&display=swap">
<style>
  :root {
    --red: #d0121b;
    --red-dark: #b50d15;
    --black: #111111;
    --white: #ffffff;
    --ink: #1a1a1a;
    --frame-grey: #8a8a8a;
    --page: #ffffff;
  }
  * { margin: 0; padding: 0; box-sizing: border-box; }
  html, body { width: 1200px; height: 991px; overflow: hidden; background: var(--page); }
  .canvas { position: relative; width: 1200px; height: 991px; }

  .hanger {
    position: absolute; top: 44px; width: 366px; height: 856px;
    background: var(--white); overflow: hidden;
    box-shadow: 0 0 0 1px #e6e6e6;
  }
  .hanger--front { left: 183px; }
  .hanger--back { left: 581px; }
  .hanger-art { position: absolute; left: 0; top: 0; }
  .side-label {
    position: absolute; top: 903px; width: 366px; text-align: center;
    font-family: "Arimo", Arial, sans-serif; font-size: 54px; line-height: 62px; color: var(--black);
  }
  .side-label--front { left: 183px; }
  .side-label--back { left: 581px; }

  .serif-red { font-family: "DM Serif Display", Georgia, serif; font-weight: 400; color: var(--red); }
  .caps { font-family: "Righteous", "Arial Black", sans-serif; text-transform: uppercase; color: var(--ink); }

  .brand-name {
    position: absolute; left: 0; top: 238px; width: 100%; text-align: center;
    font-family: "DM Serif Display", Georgia, serif; font-size: 34px; line-height: 40px; color: var(--black);
  }

  .dashed-heading { position: absolute; border: 2px dashed var(--red); text-align: center; line-height: 1.15; }
  .front-heading { left: 12px; top: 331px; width: 343px; height: 36px; font-size: 24px; padding-top: 2px; }
  .back-heading { left: 11px; top: 220px; width: 345px; height: 64px; font-size: 24px; padding-top: 3px; }

  .tagline {
    position: absolute; left: 18px; top: 391px; font-family: "Montserrat", Arial, sans-serif;
    font-weight: 800; font-size: 18px; line-height: 1.35; text-transform: uppercase; color: var(--ink);
  }
  .tagline .accent { color: var(--red); }

  .check-list { position: absolute; list-style: none; }
  .check-list li { display: flex; align-items: center; gap: 8px; }
  .check-list svg { flex: none; }
  .front-checks { left: 28px; top: 451px; }
  .front-checks li { font-size: 18.5px; height: 34.5px; }
  .back-checks { left: 16px; top: 334px; }
  .back-checks li { font-size: 13px; height: 32px; }

  .offer-title { position: absolute; left: 32px; top: 608px; font-size: 25px; line-height: 32px; }
  .offer-pill {
    position: absolute; left: 30px; top: 648px; width: 298px; height: 55px;
    background: var(--red); border-radius: 14px; padding: 7px 0 0 20px; color: var(--white);
  }
  .offer-pill .big { font-family: "Righteous", sans-serif; font-size: 22px; line-height: 24px; display: block; }
  .offer-pill .small { font-family: "Righteous", sans-serif; font-size: 13.5px; line-height: 16px; text-transform: uppercase; display: block; }

  .red-pill {
    position: absolute; background: var(--red); color: var(--white); border-radius: 16px;
    font-family: "DM Serif Display", Georgia, serif; text-align: center; font-size: 21px; line-height: 31px; height: 31px;
  }
  .services-pill { left: 41px; top: 297px; width: 264px; }
  .why-pill { left: 48px; top: 506px; width: 269px; }

  .why-list {
    position: absolute; left: 0; top: 548px; width: 100%; list-style: none; text-align: center;
    font-family: "Righteous", sans-serif; text-transform: uppercase; font-size: 12.5px; line-height: 19px; color: var(--ink);
  }

  .cta-box {
    position: absolute; left: 28px; top: 634px; width: 311px; height: 40px; border: 2px solid var(--frame-grey);
    text-align: center; font-family: "DM Serif Display", Georgia, serif; color: var(--red); font-size: 15px; line-height: 17px; padding-top: 1px;
  }
  .follow {
    position: absolute; left: 10px; top: 684px; font-family: "DM Serif Display", Georgia, serif; font-size: 15px; line-height: 19px; color: var(--black);
  }
  .social-row { position: absolute; left: 197px; top: 691px; display: flex; gap: 12px; }
  .social-icon { width: 24px; height: 24px; background: var(--red); border-radius: 4px; }

  .tear-off { position: absolute; left: 0; top: 726px; width: 100%; height: 130px; }
  .tear-brand { position: absolute; left: 0; top: 0; width: 100%; height: 46px; background: var(--red); }
  .tear-line { position: absolute; left: 0; top: 0; width: 100%; border-top: 2px dashed var(--white); }
  .tear-square { position: absolute; left: 4px; top: 4px; width: 42px; height: 40px; background: var(--white); }
  .tear-name {
    position: absolute; left: 60px; top: 14px; font-family: "Montserrat", Arial, sans-serif; font-weight: 700; font-size: 14px; line-height: 18px; color: var(--white);
  }
  .tear-call {
    position: absolute; left: 0; top: 48px; width: 100%; height: 38px; background: var(--black); color: var(--white);
    font-family: "Righteous", sans-serif; text-align: center; line-height: 38px; white-space: nowrap;
  }
  .tear-call .label { font-size: 16px; text-transform: uppercase; }
  .tear-call .phone { font-size: 22px; margin-left: 8px; }
  .tear-contacts {
    position: absolute; left: 0; top: 86px; width: 100%; height: 44px; background: var(--red); color: var(--white);
    font-family: "Arimo", Arial, sans-serif; font-weight: 400; font-size: 12.5px; text-align: center; line-height: 42px; white-space: nowrap;
  }
  .tear-contacts span + span { margin-left: 10px; }
</style>
</head>
<body>
<svg width="0" height="0" style="position:absolute">
  <defs>
    <symbol id="tick" viewBox="0 0 24 24">
      <path d="M19 9.5A9 9 0 1 1 15.5 4" fill="none" stroke="#d0121b" stroke-width="2.6" stroke-linecap="round"/>
      <path d="M7 11.5l4.5 4.5L22 4.5" fill="none" stroke="#d0121b" stroke-width="2.8" stroke-linecap="round" stroke-linejoin="round"/>
    </symbol>
    <linearGradient id="photoFront" x1="0" y1="0" x2="1" y2="1">
      <stop offset="0" stop-color="#6f6459"/><stop offset="0.5" stop-color="#4a4642"/><stop offset="1" stop-color="#9a948c"/>
    </linearGradient>
    <linearGradient id="photoBack" x1="0" y1="0" x2="1" y2="0">
      <stop offset="0" stop-color="#c9c6c1"/><stop offset="0.5" stop-color="#5a5d66"/><stop offset="1" stop-color="#3a3f4a"/>
    </linearGradient>
  </defs>
</svg>

<main class="canvas">
  <section class="hanger hanger--front">
    <svg class="hanger-art" width="366" height="330" viewBox="0 0 366 330">
      <path d="M0 0H366V250C320 262 300 230 270 230H96C66 230 46 262 0 250Z" fill="#d0121b"/>
      <path role="img" aria-label="Photo of an electrician in a hard hat working on an electrical panel" d="M0 0H366V238C320 250 300 218 270 218H96C66 218 46 250 0 238Z" fill="url(#photoFront)"/>
      <circle cx="183" cy="300" r="110" fill="#fff"/>
      <circle cx="141" cy="45" r="34" fill="#fff"/>
    </svg>
    <div class="brand-name">K&amp;T Electric</div>

    <h1 class="dashed-heading serif-red front-heading">Need a Reliable Electrician?</h1>
    <p class="tagline">Your local <span class="accent">electrical</span> expert<br>is just around the corner!</p>
    <ul class="check-list caps front-checks">
      <li><svg width="22" height="22"><use href="#tick"/></svg>Quick response times</li>
      <li><svg width="22" height="22"><use href="#tick"/></svg>Affordable rates</li>
      <li><svg width="22" height="22"><use href="#tick"/></svg>Quality workmanship</li>
      <li><svg width="22" height="22"><use href="#tick"/></svg>Fully licensed &amp; insured</li>
    </ul>
    <h2 class="offer-title serif-red">Special Offer:</h2>
    <div class="offer-pill"><span class="big">10% OFF</span><span class="small">Your first service call!</span></div>

    <div class="tear-off">
      <div class="tear-brand"><div class="tear-square"></div><div class="tear-name">K&amp;T Electric</div></div>
      <div class="tear-line"></div>
      <div class="tear-call"><span class="label">Call us today:</span><span class="phone">(555) 318-4702</span></div>
      <div class="tear-contacts"><span>info@kandtelectric.example</span><span>www.kandtelectric.example</span></div>
    </div>
  </section>

  <section class="hanger hanger--back">
    <svg class="hanger-art" width="366" height="220" viewBox="0 0 366 220">
      <path d="M0 0H366V120Q320 210 183 210Q46 210 0 120Z" fill="#d0121b"/>
      <path role="img" aria-label="Photo of an electrician in a hard hat and safety glasses wiring a distribution board" d="M0 0H366V112Q318 198 183 198Q48 198 0 112Z" fill="url(#photoBack)"/>
      <circle cx="150" cy="45" r="34" fill="#fff"/>
    </svg>

    <h1 class="dashed-heading serif-red back-heading">Don’t Let Electrical Issues<br>Keep You in the Dark!</h1>
    <div class="red-pill services-pill">Our services include:</div>
    <ul class="check-list caps back-checks">
      <li><svg width="20" height="20"><use href="#tick"/></svg>Electrical repairs &amp; troubleshooting</li>
      <li><svg width="20" height="20"><use href="#tick"/></svg>Lighting installation &amp; upgrades</li>
      <li><svg width="20" height="20"><use href="#tick"/></svg>Safety inspections &amp; code compliance</li>
      <li><svg width="20" height="20"><use href="#tick"/></svg>Energy-efficient solutions</li>
      <li><svg width="20" height="20"><use href="#tick"/></svg>24/7 emergency services</li>
    </ul>
    <div class="red-pill why-pill">Why Choose Us?</div>
    <ul class="why-list">
      <li>• Friendly, local service</li>
      <li>• Over 30 years of experience</li>
      <li>• Satisfaction guaranteed</li>
      <li>• Upfront pricing</li>
    </ul>
    <div class="cta-box">Book Your Appointment Now<br>and Claim Your 10% Discount!</div>
    <p class="follow">Follow Us for<br>More Special Offers!</p>
    <div class="social-row">
      <span class="social-icon" role="img" aria-label="Chatterpage"></span>
      <span class="social-icon" role="img" aria-label="Buzzline"></span>
      <span class="social-icon" role="img" aria-label="Pixmosaic"></span>
      <span class="social-icon" role="img" aria-label="Quibbler"></span>
    </div>

    <div class="tear-off">
      <div class="tear-brand"><div class="tear-square"></div><div class="tear-name">K&amp;T Electric</div></div>
      <div class="tear-line"></div>
      <div class="tear-call"><span class="label">Call us today:</span><span class="phone">(555) 318-4702</span></div>
      <div class="tear-contacts"><span>info@kandtelectric.example</span><span>www.kandtelectric.example</span></div>
    </div>
  </section>

  <div class="side-label side-label--front">front</div>
  <div class="side-label side-label--back">back</div>
</main>
</body>
</html>
```